Brambury Logistics

Create a modern, simple, Elegant business card design for my business.

Services: Tamo Trucks, Transport, Contract Logistics,

Industry/Entity Type

Business

Contact Information for Business Card

Include all details same as old card plus new website address: www.bramburylogistics.com.au

Requirements
Must have
• Similar colors to Logo.

```html
<!DOCTYPE html>
<html lang="en">
<head>
<meta charset="utf-8">
<title>Brambury Logistics – Business Card</title>
<link rel="stylesheet" href="https://fonts.googleapis.com/css2?family=Open+Sans:wght@400;600;700&display=swap">
<style>
  :root {
    --page-bg: #d6d6d6;
    --card-white: #ffffff;
    --brand-blue: #1a5ad8;
    --brand-blue-deep: #1440b8;
    --brand-blue-light: #3f86f0;
    --accent-blue: #1f7ad0;
    --ink-grey: #5a5a5a;
    --ink-dark: #3c3c3c;
    --rule-blue: #4a7fc0;
    --logo-silver: #c9ced6;
  }
  * { box-sizing: border-box; margin: 0; padding: 0; }
  html, body {
    width: 1200px; height: 1200px; overflow: hidden;
    background: var(--page-bg);
    font-family: "Open Sans", sans-serif;
  }
  .canvas { position: relative; width: 1200px; height: 1200px; }

  .card {
    position: absolute;
    box-shadow: 0 10px 24px rgba(0,0,0,0.18);
  }

  /* Front (blue) */
  .card-front {
    left: 520px; top: 130px; width: 600px; height: 343px;
    background:
      linear-gradient(135deg, rgba(255,255,255,0.10) 0%, rgba(255,255,255,0) 35%),
      linear-gradient(315deg, var(--brand-blue-light) 0%, var(--brand-blue) 40%, var(--brand-blue-deep) 100%);
  }
  .card-front .facet-field {
    position: absolute; inset: 0;
    background: linear-gradient(200deg, rgba(120,180,255,0.35) 0%, rgba(120,180,255,0) 45%);
  }
  .card-front .front-brand {
    position: absolute; left: 0; right: 0; top: 140px;
    display: flex; justify-content: center; align-items: center; gap: 14px;
  }
  .front-brand .brand-mark {
    width: 22px; height: 22px; background: var(--logo-silver);
  }
  .front-brand .brand-name {
    color: var(--logo-silver); font-weight: 700; font-size: 38px; letter-spacing: 0.5px;
  }
  .card-front .front-url {
    position: absolute; left: 40px; bottom: 30px;
    color: rgba(220,230,245,0.85); font-size: 17px; letter-spacing: 0.5px;
  }

  /* Back (white) */
  .card-back {
    left: 80px; top: 560px; width: 760px; height: 434px;
    background: var(--card-white);
  }
  .back-brand {
    position: absolute; left: 40px; top: 180px;
    display: flex; align-items: center; gap: 12px;
  }
  .back-brand .brand-mark { width: 20px; height: 20px; background: var(--ink-grey); }
  .back-brand .brand-name { color: var(--ink-grey); font-weight: 700; font-size: 30px; }

  .divider {
    position: absolute; left: 390px; top: 120px; width: 2px; height: 230px;
    background: var(--rule-blue);
  }

  .contact {
    position: absolute; right: 40px; top: 90px; width: 330px;
    text-align: right;
  }
  .contact .person-name {
    color: var(--ink-dark); font-size: 32px; font-weight: 700; line-height: 1;
    margin-right: 0;
  }
  .contact .person-role {
    color: var(--accent-blue); font-size: 15px; font-weight: 600; margin-top: 2px;
    margin-bottom: 22px;
  }
  .contact-row {
    display: flex; justify-content: flex-end; align-items: center; gap: 14px;
    color: var(--accent-blue); font-size: 15px; font-weight: 600;
    margin-bottom: 14px; line-height: 1.2;
  }
  .contact-row svg { width: 22px; height: 22px; flex: none; }
  .contact-row .address { text-align: right; }

  .services {
    position: absolute; left: 0; right: 0; bottom: 36px; text-align: center;
    color: var(--ink-grey); font-size: 15px; font-weight: 600; letter-spacing: 0.3px;
  }
</style>
</head>
<body>
<main class="canvas">

  <section class="card card-front" aria-label="Card front">
    <div class="facet-field" role="img" aria-label="Soft blue faceted background"></div>
    <div class="front-brand">
      <span class="brand-mark"></span>
      <span class="brand-name">Brambury Logistics</span>
    </div>
    <p class="front-url">www.bramburylogistics.com.au</p>
  </section>

  <section class="card card-back" aria-label="Card back">
    <div class="back-brand">
      <span class="brand-mark"></span>
      <span class="brand-name">Brambury Logistics</span>
    </div>

    <div class="divider"></div>

    <div class="contact">
      <p class="person-name">Daniel Harlow</p>
      <p class="person-role">Contract Manager</p>

      <div class="contact-row">
        <span>0400 555 182</span>
        <svg viewBox="0 0 24 24" fill="none" stroke="#5a5a5a" stroke-width="2"><rect x="6" y="2" width="12" height="20" rx="2"/><line x1="10" y1="18" x2="14" y2="18"/></svg>
      </div>
      <div class="contact-row">
        <span>0400 555 309</span>
        <svg viewBox="0 0 24 24" fill="#5a5a5a"><rect x="7" y="3" width="10" height="5"/><rect x="3" y="9" width="18" height="8" rx="1"/><rect x="7" y="15" width="10" height="6" fill="#fff" stroke="#5a5a5a" stroke-width="1.5"/></svg>
      </div>
      <div class="contact-row">
        <span>harlow@bramburylogistics.com.au</span>
        <svg viewBox="0 0 24 24" fill="none" stroke="#5a5a5a" stroke-width="2"><rect x="2" y="5" width="20" height="14"/><polyline points="2,5 12,13 22,5"/></svg>
      </div>
      <div class="contact-row">
        <span>www.bramburylogistics.com.au</span>
        <svg viewBox="0 0 24 24" fill="none" stroke="#5a5a5a" stroke-width="2"><circle cx="12" cy="12" r="10"/><ellipse cx="12" cy="12" rx="4" ry="10"/><line x1="2" y1="12" x2="22" y2="12"/></svg>
      </div>
      <div class="contact-row">
        <span class="address">1450 Depot Rd.<br>Perth, Western Australia</span>
        <svg viewBox="0 0 24 24" fill="#5a5a5a"><path d="M12 2a7 7 0 0 0-7 7c0 5 7 13 7 13s7-8 7-13a7 7 0 0 0-7-7zm0 10a3 3 0 1 1 0-6 3 3 0 0 1 0 6z"/></svg>
      </div>
    </div>

    <p class="services">CRANE TRUCKS • CONTRACT LOGISTICS • HOTSHOTS • PROJECT LOGISTICS</p>
  </section>

</main>
</body>
</html>
```